Bright Path Flyer Design for Virtual Online Clinic. -5.5 x 8.5 inches (half sheet)

We need a clean, modern flyer design for Bright Path, a new virtual walk-in clinic based in British Columbia. The flyer will be used in libraries, pharmacies, and community centers to help residents easily access primary care through their Bright Path NFC access card.
The flyer will ask a question : NEED A DOCTOR? This should be large and attention grabbing.
The design should clearly feature a Bright Path card image (the access card) as the centerpiece and visually show how patients can use it to book appointments. The tone should feel trustworthy, healthcare-oriented, and community-friendly — clean fonts, clear spacing, and strong readability from a distance.

Side One: This card has the NFC Access Card.
NEED A DOCTOR? (Large Font, Attention Grabbing)
How to Book an Appointment using your Bright Path Card
Step 1: Tap Your Card on Your Phone
Hold your card near the back of your phone.
It will activate automatically — no app needed.
The Bright Path scheduler will open.
Step 2: Schedule Your Appointment
Select your clinical concern.
Choose your time window.
Register (only once).
Confirm your appointment.
Step 3: Relax, we’ll take care of the rest
A doctor will call during your scheduled time.
Once booked, you’ll be able to call our office.
No emails, no texts — just a real person.
It’s that simple.
Side Two:
About Bright Path
Created by Dr. Marcus Ferrigan
Bright Path was founded to make healthcare simple and convenient. Prescription renewals. Common infections. Medical notes. And so much more.
Our doctors can address 120+ health concerns virtually — providing quality care without the waiting room. No waiting rooms. Just real doctors providing real care.
Why Patients Choose Bright Path
Easy access – book and be seen from anywhere in BC.
Effortless booking – tap your Bright Path Card to begin.
Trusted physicians – every visit is with a licensed BC family doctor.
How It Works
Book your visit — choose a time window that fits your day.
Join the queue — you’ll be called when it’s your turn.
Speak directly with your doctor — simple, secure, and stress-free.
Convenient Care for Common Concerns

Additional Details.
Please find the domain to be launched soon. I've attached the NFC card file for review, it is 85.5 mm x 54 mm. The card will be glued to the flyer.
I've attached examples of flyers but they are not the look I am seeking and I am looking for creative solutions.
Thank you!
http://brightpath-example.test/

Adult Patients in British Columbia

Healthcare

• Looking for clean lines, uniform appearance, and high legibility i.e poppins

0054AA
0677BA
7BADD7
CADEEF
E8F1F8

• Need A Doctor?
• Elegant style, not too busy, clear layout.
• Clutter, look cheap - review examples.

```html
<!DOCTYPE html>
<html lang="en">
<head>
<meta charset="utf-8">
<title>Bright Path Flyer</title>
<link rel="stylesheet" href="https://fonts.googleapis.com/css2?family=Poppins:wght@300;400;500;600;700;800&display=swap">
<style>
:root{
  --navy:#284389;
  --navy-dark:#223a7a;
  --white:#ffffff;
  --stage:#efefef;
  --mist:#e3e4e8;
  --rule:#d9dce4;
  --photo-a:#dfe7ee;
  --photo-b:#f4f7fa;
}
*{box-sizing:border-box;margin:0;padding:0}
html,body{width:1200px;height:1200px;overflow:hidden;background:var(--stage);font-family:"Poppins",sans-serif;color:var(--navy)}
.sheet{position:absolute;top:263px;width:488px;height:692px;background:var(--white);overflow:hidden;box-shadow:0 4px 12px rgba(0,0,0,.12)}
.sheet--front{left:79px}
.sheet--back{left:624px}

/* front */
.front-photo{position:absolute;left:0;top:0;width:488px;height:235px;background:linear-gradient(90deg,#c9d6e0 0%,#e6ecf1 35%,var(--white) 60%)}
.headline{position:absolute;left:174px;top:24px;font-weight:800;font-size:49px;line-height:46px;letter-spacing:-.5px;color:var(--navy)}
.front-band{position:absolute;left:0;top:235px;width:488px;height:457px;background:var(--navy)}
.access-card{position:absolute;left:97px;top:147px;width:294px;height:167px;background:var(--white);border:1px solid var(--navy)}
.access-card__art{position:absolute;left:0;top:0;width:118px;height:100%;background:linear-gradient(160deg,#2f4d98,var(--navy-dark));clip-path:polygon(0 0,100% 0,40% 100%,0 100%)}
.access-card__chip{position:absolute;right:13px;top:13px;width:12px;height:12px;background:var(--navy);border-radius:2px}
.access-card__name{position:absolute;left:108px;top:60px;font-size:28px;font-weight:500;color:var(--navy)}
.access-card__tap{position:absolute;right:45px;bottom:17px;font-size:8.5px;font-weight:400;color:var(--navy)}
.access-card__tap-icon{position:absolute;right:16px;bottom:14px}
.book-title{position:absolute;left:0;top:332px;width:488px;text-align:center;font-weight:700;font-size:24.5px;line-height:29px;color:var(--white)}
.step{position:absolute;top:409px;width:134px;height:229px;background:var(--white);border-radius:14px;overflow:hidden;text-align:center}
.step:nth-of-type(1){left:28px}
.step--1{left:28px}.step--2{left:177px}.step--3{left:327px}
.step__label{height:40px;background:var(--mist);font-weight:700;font-size:25px;line-height:40px}
.step__title{margin:13px 4px 8px;font-weight:700;font-size:12.5px;line-height:15px}
.step__line{margin:0 8px;padding:4px 0;font-size:10px;line-height:12px;font-weight:400;border-top:1px solid var(--mist)}
.step__line:first-of-type{border-top:0}
.front-help{position:absolute;left:0;top:656px;width:488px;text-align:center;color:var(--white);font-size:7.5px;line-height:13px}
.front-help strong{display:block;font-size:9.5px;font-weight:600}

/* back */
.back-photo{position:absolute;left:0;top:0;width:410px;height:164px;background:linear-gradient(90deg,var(--photo-a),var(--photo-b) 80%,var(--white))}
.back-brand{position:absolute;right:42px;top:72px;font-size:28px;font-weight:500;color:var(--navy)}
.about{position:absolute;left:29px;top:186px;width:430px}
.about__title{font-size:19.5px;font-weight:400;margin-bottom:8px}
.about p{font-size:11.3px;line-height:12.7px;font-weight:400;text-align:justify;margin-bottom:12px}
.back-band{position:absolute;left:0;top:346px;width:488px;height:297px;background:var(--navy);color:var(--white)}
.back-band__rule{position:absolute;left:259px;top:30px;width:1px;height:236px;background:rgba(255,255,255,.3)}
.col-title{position:absolute;font-size:19.5px;line-height:24px;font-weight:400}
.col-title--why{left:30px;top:20px}
.col-title--how{left:279px;top:20px}
.reason{position:absolute;left:30px;width:225px}
.reason__icon{position:absolute;left:0;top:6px}
.reason__text{margin-left:45px;font-size:12px;line-height:19px;font-weight:400}
.reason__text strong{display:block;font-weight:700}
.step-item{position:absolute;left:279px;width:190px}
.step-item::before{content:"";position:absolute;left:2px;top:6px;width:6px;height:6px;border-radius:50%;background:var(--white)}
.step-item__text{margin-left:30px;font-size:12px;line-height:17.5px;font-weight:400}
.step-item__text strong{display:block;font-weight:700;line-height:14px;margin-bottom:6px}
.back-tagline{position:absolute;left:0;top:643px;width:488px;height:40px;background:var(--mist);text-align:center;font-weight:700;font-size:14px;line-height:40px}
.back-foot{position:absolute;left:0;top:683px;width:488px;height:9px;background:var(--navy)}
</style>
</head>
<body>

<section class="sheet sheet--front">
  <div class="front-photo" role="img" aria-label="Photo of a doctor in a white coat holding a stethoscope"></div>
  <h1 class="headline">NEED<br>A DOCTOR?</h1>
  <div class="front-band"></div>

  <div class="access-card">
    <div class="access-card__art" role="img" aria-label="Card artwork with leaf illustration"></div>
    <span class="access-card__chip"></span>
    <span class="access-card__name">Bright Path</span>
    <span class="access-card__tap">Tap Here to Book</span>
    <svg class="access-card__tap-icon" width="24" height="16" viewBox="0 0 24 16" fill="none" stroke="#284389" stroke-width="1.3">
      <rect x="1" y="2" width="14" height="12" rx="2"/>
      <path d="M17 5a4 4 0 0 1 0 6M19.5 3a7 7 0 0 1 0 10"/>
    </svg>
  </div>

  <h2 class="book-title">How to Book an Appointment<br>using your Bright Path Card</h2>

  <div class="step step--1">
    <div class="step__label">Step 1</div>
    <h3 class="step__title">Tap Your Card<br>on Your Phone</h3>
    <p class="step__line">Hold your card near the back of your phone.</p>
    <p class="step__line">It will activate automatically — no app needed.</p>
    <p class="step__line">The Bright Path scheduler will open.</p>
  </div>
  <div class="step step--2">
    <div class="step__label">Step 2</div>
    <h3 class="step__title">Schedule Your<br>Appointment</h3>
    <p class="step__line">Select your clinical concern.</p>
    <p class="step__line">Choose your time window.</p>
    <p class="step__line">Register (only once).</p>
    <p class="step__line">Confirm your appointment.</p>
  </div>
  <div class="step step--3">
    <div class="step__label">Step 3</div>
    <h3 class="step__title">Relax, we’ll take<br>care of the rest</h3>
    <p class="step__line">A doctor will call during your scheduled time.</p>
    <p class="step__line">Once booked, you’ll be able to call our office.</p>
    <p class="step__line">No emails, no texts — just a real person.</p>
    <p class="step__line">It’s that simple.</p>
  </div>

  <p class="front-help">If you’re having trouble with your card or the access page, we’re her to help:<strong>support@brightpath-example.test</strong></p>
</section>

<section class="sheet sheet--back">
  <div class="back-photo" role="img" aria-label="Photo of a patient shaking hands with a doctor in a bright clinic room"></div>
  <span class="back-brand">Bright Path</span>

  <div class="about">
    <h2 class="about__title">About Bright Path</h2>
    <p>Created by Dr. Marcus Ferrigan<br>Bright Path was founded to make healthcare simple and convenient. Prescription renewals. Common infections. Medical notes. And so much more.</p>
    <p>Our doctors can address 120+ health concerns virtually — providing quality care without the waiting room. No waiting rooms. Just real doctors providing real care.</p>
  </div>

  <div class="back-band">
    <div class="back-band__rule"></div>
    <h2 class="col-title col-title--why">Why Patients Choose<br>Bright Path</h2>
    <h2 class="col-title col-title--how">How It Works</h2>

    <div class="reason" style="top:90px">
      <svg class="reason__icon" width="30" height="34" viewBox="0 0 30 34" fill="none" stroke="#fff" stroke-width="1.4">
        <path d="M15 32s-10-10-10-18a10 10 0 0 1 20 0c0 8-10 18-10 18z"/><circle cx="15" cy="14" r="3.5"/>
      </svg>
      <p class="reason__text"><strong>Easy access</strong>book and be seen from anywhere in BC.</p>
    </div>
    <div class="reason" style="top:155px">
      <svg class="reason__icon" width="28" height="38" viewBox="0 0 28 38" fill="none" stroke="#fff" stroke-width="1.4">
        <rect x="2" y="5" width="24" height="31" rx="1.5"/><path d="M8 21l5 5 8-9"/>
      </svg>
      <p class="reason__text"><strong>Effortless booking</strong>tap your Bright Path Card to begin.</p>
    </div>
    <div class="reason" style="top:220px">
      <svg class="reason__icon" width="30" height="34" viewBox="0 0 30 34" fill="none" stroke="#fff" stroke-width="1.4">
        <path d="M15 2l12 5v9c0 8-6 14-12 16C9 30 3 24 3 16V7z"/><path d="M15 11v12M9 17h12"/>
      </svg>
      <p class="reason__text"><strong>Trusted physicians</strong>every visit is with a licensed BC family doctor.</p>
    </div>

    <div class="step-item" style="top:56px">
      <p class="step-item__text"><strong>Book your visit</strong>you’ll be called when it’s your turn</p>
    </div>
    <div class="step-item" style="top:129px">
      <p class="step-item__text"><strong>Join the queue</strong>choose a time window that fits your day.</p>
    </div>
    <div class="step-item" style="top:200px">
      <p class="step-item__text"><strong>Speak directly with your doctor</strong>simple, secure, and stress-free.</p>
    </div>
  </div>

  <div class="back-tagline">Convenient Care for Common Concerns</div>
  <div class="back-foot"></div>
</section>

</body>
</html>
```